Business Card Professional Clean - Lumavault

Create a business card for my company that deals with Cryptocurrencies. I have a few designs ideas that I'd like to be implemented. Thanks! I will include the logo files, and a link to the design styles that I like.

Target Market(s)

Professionals

Industry/Entity Type

Consulting

Contact Information for Business Card

Name: Mark Dunn
Title: CEO/Technical Director
Phone: (587)943-0586
E-mail: mdunn@lumavault.ca
Address: Suite 512, 208-3370 Harwood Avenue NW

Twitter: @LumaVaultHQ
Instagram: lumavaulthq

Colors
92b5d7
3276b5
33a6d7
85acd3
85cae6
0592cd

Requirements
Must have
• Some colors that match with the logo and the pictures I put in below.
• Ideally the finished product would look something like the attachments showing the color gradient I want.
Nice to have
• Please see some of the attachments I've included. This is very close to the final product that I would like to see. If someone could recreate something like those I would definitely feel pretty good about it.
• For the instagram and twitter please use the symbols/icon to represent it on the card.
Should not have
• No crazy colors and unprofessional styles. I just want clear info. Don't go outside the boundaries of the colors in the attachment and we should be good. No crazy weird fonts either.

```html
<!DOCTYPE html>
<html lang="en">
<head>
<meta charset="utf-8">
<title>Lumavault Business Card</title>
<link rel="stylesheet" href="https://fonts.googleapis.com/css2?family=Source+Sans+3:wght@400;600;700&display=swap">
<style>
  :root {
    --stage: #2b2d31;
    --card-white: #ffffff;
    --navy: #3b4a5f;
    --navy-deep: #34435a;
    --brand-blue: #1d5fb0;
    --text-grey: #5b6470;
    --contact-text: #e6ebf1;
  }
  * { margin: 0; padding: 0; box-sizing: border-box; }
  html, body {
    width: 1200px; height: 900px; overflow: hidden;
    background: var(--stage);
    font-family: "Source Sans 3", Arial, sans-serif;
  }
  .card {
    position: absolute; left: 250px;
    width: 700px; height: 400px;
    border-radius: 4px; overflow: hidden;
    box-shadow: 0 14px 30px rgba(0,0,0,.45);
  }
  .card--front { top: 40px; background: var(--card-white); }
  .card--back  { top: 460px; background: var(--navy); }

  .front-panel { position: absolute; inset: 0; }

  .brand {
    position: absolute; display: flex; align-items: center; gap: 14px;
    font-weight: 600; letter-spacing: 2px;
  }
  .brand__mark { display: block; border: 3px solid currentColor; }
  .brand--front { left: 40px; top: 48px; color: var(--brand-blue); font-size: 38px; }
  .brand--front .brand__mark { width: 30px; height: 30px; }
  .brand--back {
    left: 50%; top: 50%; transform: translate(-50%, -50%);
    color: var(--card-white); font-size: 60px;
  }
  .brand--back .brand__mark { width: 50px; height: 50px; }

  .contact-list {
    position: absolute; left: 34px; top: 222px;
    list-style: none; color: var(--contact-text);
    font-size: 16px; line-height: 1.35;
  }
  .contact-list li { display: flex; align-items: flex-start; gap: 10px; margin-bottom: 3px; }
  .contact-icon { width: 14px; height: 14px; flex: none; margin-top: 3px; fill: var(--contact-text); }

  .holder {
    position: absolute; right: 40px; top: 150px; text-align: right;
    z-index: 2;
  }
  .holder__name {
    color: var(--brand-blue); font-weight: 700; font-size: 34px; letter-spacing: 1px;
  }
  .holder__title { color: var(--text-grey); font-size: 17px; margin-top: 2px; }

  .accent-square {
    position: absolute; left: 472px; top: 285px;
    width: 140px; height: 140px;
    border: 12px solid var(--brand-blue);
  }
</style>
</head>
<body>
  <section class="card card--front" aria-label="Business card front">
    <svg class="front-panel" viewBox="0 0 700 400" preserveAspectRatio="none" aria-hidden="true">
      <polygon points="0,190 385,125 385,400 0,400" fill="var(--navy)"/>
    </svg>

    <div class="brand brand--front"><span class="brand__mark"></span>Lumavault</div>

    <ul class="contact-list">
      <li><svg class="contact-icon" viewBox="0 0 16 16"><path d="M3 1h3l1.5 4-2 1.2a9 9 0 0 0 4.3 4.3L11 8.5l4 1.5v3a2 2 0 0 1-2 2A13 13 0 0 1 1 3a2 2 0 0 1 2-2z"/></svg>(587)943-0586</li>
      <li><svg class="contact-icon" viewBox="0 0 16 16"><path d="M1 3h14v10H1z M2 4.5v.3l6 4 6-4v-.3z" fill-rule="evenodd"/></svg>mdunn@lumavault.ca</li>
      <li><svg class="contact-icon" viewBox="0 0 16 16"><circle cx="8" cy="8" r="6"/></svg>@LumaVaultHQ</li>
      <li><svg class="contact-icon" viewBox="0 0 16 16"><rect x="2" y="2" width="12" height="12" rx="2"/></svg>lumavaulthq</li>
      <li><svg class="contact-icon" viewBox="0 0 16 16"><path d="M8 1l7 6h-2v8h-4v-5H7v5H3V7H1z"/></svg><span>Suite 512, 208-3370<br>Harwood Avenue NW</span></li>
    </ul>

    <div class="accent-square" aria-hidden="true"></div>

    <div class="holder">
      <p class="holder__name">MARK DUNN</p>
      <p class="holder__title">CEO/Technical Director</p>
    </div>
  </section>

  <section class="card card--back" aria-label="Business card back">
    <div class="brand brand--back"><span class="brand__mark"></span>Lumavault</div>
  </section>
</body>
</html>
```